Storm Restoration Contractor needs a professional business card design

Looking for a professional business card design. Not looking for your cheapo MS Word standard ones that are readily available. Dont want it to be cookie cutter look like ones readily available online. We just recently changed our logo and want to freshen up all our documents. Our company handles restoring a property back to a pre-loss condition after a storm damages it. For example, wind, hail, flood, fire losses.

Target Market(s)

Property Owners, Homeowners, Property Owners, Commercial Property Owners, Property Management Companies, Hail and Wind Damaged Properties

Industry/Entity Type

Construction Company

Contact Information for Business Card

Bramwell Outworks
555-418-7302
555-418-9047 fax
www.bramwelloutworks.example
info@bramwelloutworks.example

Requirements
Must have
• Clean, Professional, fresh look
• Storm Restoration, Roofing, Siding, Windows
Nice to have
• If there is a way to incorporate storms that may be cool.

```html
<!DOCTYPE html>
<html lang="en">
<head>
<meta charset="utf-8">
<title>Bramwell Outworks — Business Card</title>
<link rel="stylesheet" href="https://fonts.googleapis.com/css2?family=Open+Sans:wght@400;600;700&display=swap">
<style>
  :root {
    --brand-blue: #1f95d2;
    --brand-blue-deep: #0f6fae;
    --slate: #5b5e62;
    --slate-light: #8a8d91;
    --paper: #f7f7f7;
    --backdrop: #e8e6e2;
    --white: #ffffff;
  }
  * { box-sizing: border-box; margin: 0; padding: 0; }
  html, body { width: 1200px; height: 780px; overflow: hidden; }
  body {
    background: var(--backdrop);
    font-family: "Open Sans", Arial, sans-serif;
    position: relative;
  }
  .card {
    position: absolute;
    top: 240px;
    width: 520px;
    height: 300px;
    overflow: hidden;
    border-radius: 3px;
    box-shadow: 0 2px 8px rgba(0,0,0,0.12);
  }
  .card-front { left: 50px; background: var(--paper); }
  .card-back {
    left: 630px;
    background: linear-gradient(160deg, #2aa3de 0%, var(--brand-blue) 45%, var(--brand-blue-deep) 100%);
    color: var(--white);
  }

  /* front */
  .front-brand {
    height: 120px;
    display: flex;
    align-items: center;
    padding-left: 34px;
    gap: 16px;
  }
  .brand-dot {
    width: 54px; height: 54px;
    border-radius: 50%;
    border: 6px solid var(--brand-blue);
  }
  .brand-divider { width: 2px; height: 58px; background: var(--brand-blue); }
  .brand-name {
    font-weight: 700;
    font-size: 30px;
    line-height: 1.0;
    color: var(--brand-blue);
    text-transform: uppercase;
    letter-spacing: 1px;
  }
  .name-band {
    height: 34px;
    background: var(--brand-blue);
    color: var(--white);
    display: flex;
    align-items: center;
    padding-left: 34px;
    font-size: 15px;
  }
  .name-band .person { font-weight: 700; text-transform: uppercase; letter-spacing: 0.5px; }
  .name-band .role { font-weight: 400; margin-left: 6px; }
  .contact-panel {
    height: 146px;
    background: linear-gradient(180deg, #6a6d71 0%, var(--slate) 100%);
    color: var(--white);
    padding: 14px 34px;
    display: flex;
    gap: 14px;
  }
  .contact-icons { display: flex; flex-direction: column; justify-content: flex-end; gap: 4px; padding-bottom: 4px; }
  .contact-icons svg { width: 16px; height: 16px; display: block; }
  .contact-lines { font-size: 13px; line-height: 1.45; }

  /* back */
  .back-brand {
    display: flex;
    align-items: center;
    justify-content: center;
    gap: 16px;
    margin-top: 48px;
  }
  .back-brand .brand-dot { border-color: var(--white); }
  .back-brand .brand-divider { background: var(--white); }
  .back-brand .brand-name { color: var(--white); }
  .service-icons {
    display: flex;
    justify-content: center;
    gap: 26px;
    margin-top: 34px;
  }
  .service-icons svg { width: 52px; height: 52px; display: block; }
  .service-line {
    text-align: center;
    margin-top: 26px;
    font-size: 15px;
    letter-spacing: 0.4px;
  }
</style>
</head>
<body>

<section class="card card-front" aria-label="Business card front">
  <div class="front-brand">
    <div class="brand-dot"></div>
    <div class="brand-divider"></div>
    <div class="brand-name">Bramwell<br>Outworks</div>
  </div>
  <div class="name-band">
    <span class="person">Dorian Halvek</span><span class="role">| Project Manager</span>
  </div>
  <div class="contact-panel">
    <div class="contact-icons">
      <svg viewBox="0 0 16 16" aria-label="Phone"><rect width="16" height="16" rx="2" fill="var(--brand-blue)"/><path d="M5 4l2 0 1 2-1 1a5 5 0 0 0 2 2l1-1 2 1 0 2c-4 0-7-3-7-7z" fill="#fff"/></svg>
      <svg viewBox="0 0 16 16" aria-label="Fax"><rect width="16" height="16" rx="2" fill="var(--brand-blue)"/><rect x="4" y="5" width="8" height="7" fill="#fff"/><rect x="5" y="3" width="6" height="3" fill="#fff"/></svg>
      <svg viewBox="0 0 16 16" aria-label="Email"><rect width="16" height="16" rx="2" fill="var(--brand-blue)"/><rect x="3" y="5" width="10" height="7" fill="#fff"/><path d="M3 5l5 4 5-4" stroke="var(--brand-blue)" fill="none"/></svg>
      <svg viewBox="0 0 16 16" aria-label="Website"><rect width="16" height="16" rx="2" fill="var(--brand-blue)"/><circle cx="8" cy="8" r="5" fill="none" stroke="#fff"/><path d="M3 8h10M8 3v10" stroke="#fff"/></svg>
    </div>
    <div class="contact-lines">
      <div>410 Larkfield Ave, Suite 12</div>
      <div>Fenmore, IL 60999</div>
      <div>555-418-7302</div>
      <div>555-418-6621</div>
      <div>dhalvek@bramwelloutworks.example</div>
      <div>www.bramwelloutworks.example</div>
    </div>
  </div>
</section>

<section class="card card-back" aria-label="Business card back">
  <div class="back-brand">
    <div class="brand-dot"></div>
    <div class="brand-divider"></div>
    <div class="brand-name">Bramwell<br>Outworks</div>
  </div>
  <div class="service-icons">
    <svg viewBox="0 0 52 52" aria-label="Storm restoration"><circle cx="26" cy="26" r="24" fill="none" stroke="#fff" stroke-width="2"/><path d="M15 17h22M17 22h17M19 27h13M21 32h9M23 37h5" stroke="#fff" stroke-width="2.5" stroke-linecap="round"/></svg>
    <svg viewBox="0 0 52 52" aria-label="Water damage"><circle cx="26" cy="26" r="24" fill="none" stroke="#fff" stroke-width="2"/><path d="M26 13c5 8 8 12 8 16a8 8 0 0 1-16 0c0-4 3-8 8-16z" fill="#fff"/></svg>
    <svg viewBox="0 0 52 52" aria-label="Roofing"><circle cx="26" cy="26" r="24" fill="none" stroke="#fff" stroke-width="2"/><path d="M13 27l13-12 13 12h-4v11H17V27z" fill="#fff"/></svg>
    <svg viewBox="0 0 52 52" aria-label="Windows"><circle cx="26" cy="26" r="24" fill="none" stroke="#fff" stroke-width="2"/><rect x="16" y="16" width="20" height="20" fill="none" stroke="#fff" stroke-width="2.5"/><path d="M26 16v20M16 26h20" stroke="#fff" stroke-width="2"/></svg>
  </div>
  <p class="service-line">Storm Restoration | Roofing | Siding | Windows</p>
</section>

</body>
</html>
```